Label - Australian Extra Virgin Olive Oil

I'm seeking a front and back label to apply to bottles/tins of my olive oil. They will be applied to green bottles of various sizes and also white tins. The labels will have the dimensions 70 x 120mm and printed at 600dpi on adhesive labels with metalised backing. With this material, any area which is not colored on the label will show through as silver - the design may make use of this feature. There are some obligatory labeling requirements in Australia including a logo showing the proportion of Australian content, and an indication of the harvest date - the design will need to make allowance for this. Also, since the label will be used in subsequent years and on various sizes of product, I need to be able to alter this with each print run.I have a logo to use on the front label and another I would like to use on the back as this latter one will tie in with other future products (non olive oil).
The text for the back label
"Tallowby Creek is a family run enterprise. Our olives are grown on the banks of the Wendrake River in Central Victoria and processed locally
email; quietheron@pelinet.com.au
text needed for the front label design
"Australian Extra-Virgin Olive Oil"

```html
<!DOCTYPE html>
<html lang="en">
<head>
<meta charset="utf-8">
<title>Tallowby Creek – Australian Extra Virgin Olive Oil Label</title>
<link rel="stylesheet" href="https://fonts.googleapis.com/css2?family=Montserrat:wght@400;600;700&display=swap">
<style>
  :root {
    --page: #ffffff;
    --label-dark: #2f6d24;
    --label-mid: #4f8f2c;
    --label-light: #7fb13a;
    --trim-lime: #c9e35a;
    --trim-white: #f4f9e4;
    --band-white: #ffffff;
    --ink-green: #3a8f3a;
    --ink-white: #ffffff;
    --ink-dark: #333333;
  }
  html, body {
    margin: 0;
    padding: 0;
    width: 1200px;
    height: 1000px;
    overflow: hidden;
    background: var(--page);
  }
  .label-canvas {
    display: block;
    width: 1200px;
    height: 1000px;
  }
  .label-body { fill: var(--label-dark); }
  .trim-outer { fill: none; stroke: var(--trim-lime); stroke-width: 5; }
  .trim-inner { fill: none; stroke: var(--trim-white); stroke-width: 1.5; }
  .title-band { fill: var(--band-white); }
  .band-edge { stroke: var(--trim-lime); stroke-width: 3; }
  .divider-rule { stroke: var(--ink-green); stroke-width: 2; }
  .volume-box { fill: var(--band-white); }
  .brand-name {
    font-family: 'Montserrat', sans-serif;
    font-weight: 600;
    font-size: 52px;
    fill: var(--ink-white);
  }
  .word-origin {
    font-family: 'Montserrat', sans-serif;
    font-weight: 700;
    font-size: 62px;
    fill: var(--ink-white);
  }
  .word-grade {
    font-family: 'Montserrat', sans-serif;
    font-weight: 700;
    font-size: 78px;
    fill: var(--ink-green);
  }
  .word-product {
    font-family: 'Montserrat', sans-serif;
    font-weight: 400;
    font-size: 104px;
    fill: var(--ink-white);
  }
  .volume-caption {
    font-family: 'Montserrat', sans-serif;
    font-weight: 600;
    font-size: 13px;
    fill: var(--ink-dark);
  }
</style>
</head>
<body>
<svg class="label-canvas" viewBox="0 0 1200 1000" xmlns="http://www.w3.org/2000/svg">
  <defs>
    <linearGradient id="oilGlow" x1="0" y1="0" x2="1" y2="1">
      <stop offset="0" stop-color="#3f7f2a"/>
      <stop offset="0.5" stop-color="#5e9a30"/>
      <stop offset="1" stop-color="#2f6d24"/>
    </linearGradient>
    <radialGradient id="sprigTone" cx="0.5" cy="0.5" r="0.5">
      <stop offset="0" stop-color="#8bbf3a"/>
      <stop offset="1" stop-color="#8bbf3a" stop-opacity="0"/>
    </radialGradient>
  </defs>

  <!-- label outline -->
  <path class="label-body" d="M358,8 H842 A40 40 0 0 0 882 48 V952 A40 40 0 0 0 842 992 H358 A40 40 0 0 0 318 952 V48 A40 40 0 0 0 358 8 Z"/>

  <!-- background oil photograph area -->
  <path role="img" aria-label="Close-up photograph of golden-green olive oil pouring" fill="url(#oilGlow)"
        d="M366,27 H834 A32 32 0 0 0 864 57 V943 A32 32 0 0 0 834 973 H366 A32 32 0 0 0 336 943 V57 A32 32 0 0 0 366 27 Z"/>

  <!-- trim lines -->
  <path class="trim-outer" d="M366,27 H834 A32 32 0 0 0 864 57 V943 A32 32 0 0 0 834 973 H366 A32 32 0 0 0 336 943 V57 A32 32 0 0 0 366 27 Z"/>
  <path class="trim-inner" d="M370,33 H830 A30 30 0 0 0 858 61 V939 A30 30 0 0 0 830 967 H370 A30 30 0 0 0 342 939 V61 A30 30 0 0 0 370 33 Z"/>

  <!-- brand -->
  <text class="brand-name" x="600" y="265" text-anchor="middle">Tallowby Creek</text>

  <!-- origin -->
  <text class="word-origin" x="600" y="385" text-anchor="middle">AUSTRALIAN</text>

  <!-- grade band -->
  <rect class="title-band" x="340" y="414" width="520" height="166"/>
  <line class="band-edge" x1="340" y1="414" x2="860" y2="414"/>
  <line class="band-edge" x1="340" y1="580" x2="860" y2="580"/>
  <text class="word-grade" x="600" y="492" text-anchor="middle">EXTRA</text>
  <line class="divider-rule" x1="413" y1="500" x2="800" y2="500"/>
  <text class="word-grade" x="600" y="570" text-anchor="middle">VIRGIN</text>

  <!-- olive sprig ornaments -->
  <ellipse role="img" aria-label="Olive sprig ornament" cx="810" cy="445" rx="45" ry="32" fill="url(#sprigTone)"/>
  <ellipse role="img" aria-label="Olive sprig ornament" cx="385" cy="548" rx="45" ry="32" fill="url(#sprigTone)"/>

  <!-- product -->
  <text class="word-product" x="600" y="700" text-anchor="middle">OLIVE</text>
  <text class="word-product" x="600" y="788" text-anchor="middle">OIL</text>

  <!-- volume field -->
  <rect class="volume-box" x="449" y="832" width="306" height="65" rx="16"/>
  <text class="volume-caption" x="462" y="874">vol :</text>
</svg>
</body>
</html>
```